Webbanner-Design für regionale Geschenkkarte
Zielgruppe
Die Lindgrün-Karte ist eine regionale Geschenkkarte für PLZ 52 zur Unterstützung aller inhabergeführten Geschäfte wie Einzelhandel, Restaurants und Dienstleister
Zielgruppe sind all diejenigen, die eine Geschenkkarte suchen und die das regionale den Internetriesen und Großfilialisten vorziehen. Zudem können die Verschenker auch ein individuelles Design erhalten. Über unsere App können die Kunden Bilder hochladen, individuelle Texte auf die Karte drucken lassen etc.
Aufgabenstellung
Regionale Geschenkkarte PLZ 52 (www.lindgruen-karte.example) , individuelles Design, verschiedene Bannergrößen wichtig zum Einbau auf Unterseiten von Kunden der lindgruenpix.example, zudem sollen die Banner auch direkt auf Seiten der Kunden eingebaut werden können. Nach dem Motto: wir akzeptieren die Lindgrün Geschenkkarte bzw. wir sind dabei

```html
<!DOCTYPE html>
<html lang="de">
<head>
<meta charset="utf-8">
<title>Lindgrün-Karte – Plakat</title>
<link rel="stylesheet" href="https://fonts.googleapis.com/css2?family=Open+Sans:wght@700&family=PT+Sans+Narrow:wght@700&display=swap">
<style>
  :root {
    --canvas-bg: #ededed;
    --red-deep: #a30a27;
    --red-mid: #c81e3a;
    --red-card: #d3253f;
    --red-light: #e84a5f;
    --white: #ffffff;
    --url-red: #9e0f2a;
    --photo-top: #e9d6cf;
    --photo-bottom: #b9dde3;
  }
  * { margin: 0; padding: 0; box-sizing: border-box; }
  html, body {
    width: 1200px; height: 1200px; overflow: hidden;
    background: var(--canvas-bg);
  }
  .poster {
    position: absolute; left: 201px; top: 35px;
    width: 798px; height: 1130px;
    background: linear-gradient(180deg, var(--red-deep) 0%, var(--red-mid) 30%, #d24a5e 40%, var(--white) 56%);
    overflow: hidden;
  }
  .brand {
    position: absolute; left: 63px; top: 32px;
    display: flex; align-items: center; gap: 30px;
  }
  .brand-square {
    width: 147px; height: 147px; border-radius: 14px;
    background: var(--red-light);
  }
  .brand-name {
    font-family: "Open Sans", sans-serif; font-weight: 700;
    font-size: 47px; color: var(--white); letter-spacing: 0.5px;
  }
  .headline {
    position: absolute; left: 0; right: 0; top: 222px;
    text-align: center;
    font-family: "PT Sans Narrow", sans-serif; font-weight: 700;
    font-size: 46px; color: var(--white);
  }
  .gift-card {
    position: absolute; left: 52px; top: 307px;
    width: 706px; height: 455px; border-radius: 26px;
    background: radial-gradient(ellipse at 40% 75%, #f7dde1 0%, var(--red-light) 45%, var(--red-card) 75%, var(--red-deep) 100%);
    box-shadow: 0 4px 10px rgba(0,0,0,0.15);
  }
  .gift-card__domain {
    position: absolute; right: 18px; top: 100px;
    font-family: "Open Sans", sans-serif; font-weight: 700;
    font-size: 18px; color: var(--white);
  }
  .gift-card__band {
    position: absolute; left: 335px; right: 0; top: 132px; height: 41px;
    background: var(--white);
    display: flex; align-items: center; justify-content: flex-end; padding-right: 18px;
    font-family: "Open Sans", sans-serif; font-weight: 700;
    font-size: 34px; color: var(--url-red);
  }
  .gift-card__sms {
    position: absolute; right: 26px; bottom: 20px;
    font-family: "Open Sans", sans-serif; font-size: 22px; color: var(--white);
  }
  .photo {
    position: absolute; left: 0; top: 469px;
    width: 659px; height: 585px;
    background: linear-gradient(180deg, var(--photo-top) 0%, #dcc0b4 45%, var(--photo-bottom) 75%, #a8d3da 100%);
    border-top-right-radius: 220px;
  }
  .footer {
    position: absolute; left: 0; right: 0; bottom: 0; height: 76px;
    background: var(--white);
    display: flex; align-items: center; justify-content: center;
    font-family: "PT Sans Narrow", sans-serif; font-weight: 700;
    font-size: 50px; color: var(--url-red);
  }
</style>
</head>
<body>
  <main class="poster">
    <div class="brand">
      <div class="brand-square"></div>
      <span class="brand-name">Lindgrün-Karte</span>
    </div>
    <h1 class="headline">Die regionale Geschenkkarte für PLZ 52</h1>
    <div class="gift-card">
      <span class="gift-card__domain">lindgruen-karte.example</span>
      <div class="gift-card__band">Geschenkkarte</div>
      <span class="gift-card__sms">SMS</span>
    </div>
    <div class="photo" role="img" aria-label="Foto: lächelnde Frau in hellblauem Oberteil hält eine rote Geschenkkarte in die Kamera"></div>
    <footer class="footer">www.lindgruen-karte.example</footer>
  </main>
</body>
</html>
```